Calcutta Flyer

Need a 1 pager flyer to promote our upcoming Brindlewood Stakes Calcutta.
I have attached our flyer from last year to give you some ideas.
This years event is being held at the Harrow Vale Inn (Logo provided) and is being sponsored by Tarwick Turf Partnerships (2 logos provided).
We (Corvale Herons Veterans Club 'The Nest') Logo provided are the Calcutta's host and benefactor to the tune of 10% of the overall money raised.
This years event is on Monday 4th November 2024 @ 6.30PM. All other details on last years flyer are relevant for this years flyer as well.

```html
<!DOCTYPE html>
<html lang="en">
<head>
<meta charset="utf-8">
<title>Brindlewood Stakes Calcutta</title>
<link rel="stylesheet" href="https://fonts.googleapis.com/css2?family=Anton&family=Cinzel:wght@500;700&family=Montserrat:wght@700;800&display=swap">
<style>
  :root {
    --ink: #050505;
    --paper: #ffffff;
    --gold: #d4a52a;
    --gold-light: #f5c518;
    --gold-dark: #b98d2a;
    --navy: #12294a;
    --blue: #1f4d80;
    --stage: #d9d6d2;
  }
  * { margin: 0; padding: 0; box-sizing: border-box; }
  html, body { width: 1200px; height: 1117px; overflow: hidden; }
  body { background: var(--stage); font-family: "Montserrat", sans-serif; }

  .flyer {
    position: absolute; left: 206px; top: 0;
    width: 787px; height: 1117px;
    background: var(--ink); overflow: hidden; color: var(--paper);
  }
  .flyer > * { position: absolute; }

  .backdrop { left: 0; top: 0; width: 787px; height: 1117px; }

  .host {
    left: 90px; top: 52px;
    display: flex; align-items: center; gap: 10px; white-space: nowrap;
  }
  .host-dot { width: 18px; height: 18px; border-radius: 50%; background: var(--paper); flex: none; }
  .host-name { font-weight: 800; font-size: 22px; letter-spacing: 0.5px; color: var(--paper); }

  .star { left: 528px; top: 282px; width: 236px; height: 228px; }

  .athletes {
    left: 210px; top: 400px; width: 555px; height: 335px;
    border-radius: 10px;
    background: linear-gradient(100deg, #6b3a22 0%, #9a6a48 28%, #d8d5d0 55%, #5c7fae 78%, #d4a52a 100%);
  }

  .headline {
    font-family: "Anton", sans-serif; text-transform: uppercase; white-space: nowrap;
    line-height: 1; transform: rotate(-5deg) skewX(-10deg); transform-origin: left bottom;
  }
  .headline-calcutta { left: 236px; top: 40px; font-size: 116px; color: var(--paper); }
  .headline-event {
    left: 70px; top: 176px; font-size: 100px;
    background: linear-gradient(180deg, var(--gold-light), var(--gold-dark));
    -webkit-background-clip: text; background-clip: text; color: transparent;
  }
  .headline-event span { display: block; }
  .headline-event span + span { margin-left: 150px; margin-top: -4px; }

  .tickets {
    left: 45px; top: 588px; width: 150px; height: 150px; border-radius: 50%;
    background: var(--paper); border: 4px solid var(--navy);
    box-shadow: 0 6px 10px rgba(0,0,0,0.25);
    display: flex; flex-direction: column; align-items: center; justify-content: center;
  }
  .tickets-label { font-weight: 800; font-size: 17px; color: var(--ink); letter-spacing: 0.5px; }
  .tickets-price { font-weight: 800; font-size: 58px; line-height: 1; color: var(--gold-dark); }

  .date-band {
    left: 0; top: 767px; width: 787px; height: 100px;
    background: linear-gradient(90deg, var(--gold-dark), var(--gold) 60%, #c9a33a);
    text-align: center; padding-top: 26px; white-space: nowrap;
    font-weight: 800; font-size: 30px; letter-spacing: 0.3px; color: var(--paper);
  }
  .benefit {
    left: 52px; top: 846px; width: 684px; height: 46px;
    background: var(--navy); border: 2px solid var(--gold); border-radius: 6px;
    display: flex; align-items: center; justify-content: center; white-space: nowrap;
    font-weight: 800; font-size: 17px; letter-spacing: 0.3px; color: var(--paper);
  }
  .benefit b { color: var(--gold-light); font-weight: 800; margin-right: 6px; }

  .venue-note {
    left: 62px; top: 950px; width: 240px; text-align: center; white-space: nowrap;
    font-weight: 800; font-size: 16px; line-height: 21px; color: var(--paper);
  }
  .venue-note em { font-style: normal; color: var(--gold-light); }

  .venue-name {
    left: 320px; top: 950px; width: 220px; text-align: center;
    font-family: "Cinzel", serif; font-weight: 700; font-size: 25px; line-height: 31px; color: var(--paper);
  }

  .sponsor-frame { left: 0; top: 0; width: 787px; height: 1117px; }
  .sponsor { left: 575px; top: 952px; width: 212px; text-align: center; }
  .sponsor-label { font-family: "Cinzel", serif; font-weight: 500; font-size: 14px; letter-spacing: 1px; color: var(--gold); }
  .sponsor-name {
    margin-top: 26px; font-family: "Cinzel", serif; font-weight: 700;
    font-size: 20px; line-height: 26px; color: var(--paper);
  }

  .web {
    left: 52px; top: 1066px; white-space: nowrap;
    display: flex; align-items: baseline; gap: 8px;
  }
  .web-url { font-weight: 800; font-size: 21px; color: var(--paper); }
  .web-terms { font-weight: 700; font-size: 9px; color: var(--paper); }
</style>
</head>
<body>
<main class="flyer">
  <svg class="backdrop" viewBox="0 0 787 1117" aria-hidden="true">
    <polygon points="0,692 787,511 787,767 0,767" fill="#ffffff"/>
    <polygon points="0,867 334,867 0,943" fill="#ffffff"/>
    <polygon points="0,1044 540,1044 526,1117 0,1117" fill="#1f4d80"/>
  </svg>

  <div class="host">
    <span class="host-dot"></span>
    <span class="host-name">THE NEST</span>
  </div>

  <div class="athletes" role="img" aria-label="Sports collage: jockey on a racehorse, hockey, basketball and football players, a sprinter, a chequered flag and gold trophies"></div>

  <svg class="star" viewBox="0 0 270 260" aria-hidden="true">
    <polygon points="135,8 166,98 262,100 186,158 213,250 135,196 57,250 84,158 8,100 104,98"
      fill="none" stroke="#d4a52a" stroke-width="14" stroke-linejoin="miter"/>
  </svg>

  <h1 class="headline headline-calcutta">Calcutta</h1>
  <h2 class="headline headline-event"><span>Brindlewood</span><span>Stakes</span></h2>

  <div class="tickets">
    <span class="tickets-label">TICKETS</span>
    <span class="tickets-price">$5</span>
  </div>

  <div class="date-band">MONDAY 4TH NOVEMBER 2024 @ 6.30PM</div>
  <div class="benefit"><b>$10%</b> OF PROFITS GOING TO THE CORVALE HERONS VETERANS</div>

  <p class="venue-note">THIS YEARS EVENT<br>IS BEING HELD AT<br><em>THE HARROW VALE INN</em></p>
  <div class="venue-name">HARROW VALE<br>INN</div>

  <svg class="sponsor-frame" viewBox="0 0 787 1117" aria-hidden="true">
    <path d="M522,1117 L578,948 Q584,932 602,932 L787,932" fill="none" stroke="#ffffff" stroke-width="4"/>
  </svg>
  <div class="sponsor">
    <div class="sponsor-label">SPONSORED BY</div>
    <div class="sponsor-name">TARWICK TURF<br>PARTNERSHIPS</div>
  </div>

  <div class="web">
    <span class="web-url">www.corvalenest.com.au</span>
    <span class="web-terms">( FOR TERMS &amp; CONDITIONS )</span>
  </div>
</main>
</body>
</html>
```